Business Card Design Project

We need a business card design for a new boutique consulting company, LumaConsulting. Our new logo has just been designed and we are looking for simple, clean looking business cards. Logo attached

Industry/Entity Type

Boutique

Requirements
Must have
• There must be room for each card to have the following details:
Name
Title
Address - 2 lines
Phone number
Email address
Website address

Nice to have
• May have something on the back of the buisness card - emphasing the word "Luma".

```html
<!DOCTYPE html>
<html lang="en">
<head>
<meta charset="utf-8">
<title>LumaConsulting Business Card</title>
<link href="https://fonts.googleapis.com/css2?family=Arimo:ital,wght@0,400;0,700;1,400&display=swap" rel="stylesheet">
<style>
  :root {
    --backdrop: #e8e5e1;
    --card-dark: #262626;
    --card-white: #ffffff;
    --brand-green: #62b22f;
    --logo-grey: #6e6e6e;
    --ink: #111111;
    --pattern-dark: #2c2d2c;
    --pattern-green: #34402b;
    --back-word: #5f8a3a;
  }
  html, body {
    margin: 0;
    padding: 0;
    width: 1086px;
    height: 1200px;
    overflow: hidden;
    background: var(--backdrop);
    font-family: "Arimo", Arial, sans-serif;
  }
  .canvas {
    position: relative;
    width: 1086px;
    height: 1200px;
  }
  .card-front {
    position: absolute;
    left: 43px;
    top: 32px;
    width: 1004px;
    height: 536px;
    background: var(--card-dark);
  }
  .front-panel {
    position: absolute;
    left: 62px;
    top: 61px;
    width: 867px;
    height: 404px;
    background: var(--card-white);
    border: 4px solid var(--brand-green);
  }
  .logo {
    position: absolute;
    left: 0;
    right: 0;
    top: 40px;
    display: flex;
    justify-content: center;
    align-items: center;
    gap: 16px;
  }
  .logo-mark {
    width: 30px;
    height: 30px;
    background: var(--brand-green);
  }
  .logo-name {
    font-size: 70px;
    color: var(--logo-grey);
    line-height: 1;
    letter-spacing: -1px;
  }
  .person {
    position: absolute;
    left: 0;
    right: 0;
    top: 150px;
    text-align: center;
    color: var(--ink);
  }
  .person-name {
    font-size: 46px;
    line-height: 1.05;
  }
  .person-title {
    font-size: 27px;
    font-style: italic;
  }
  .contact-phones,
  .contact-web,
  .contact-address {
    position: absolute;
    bottom: 6px;
    font-style: italic;
    font-size: 20px;
    line-height: 24px;
    color: var(--ink);
  }
  .contact-phones { left: 8px; }
  .contact-web {
    left: 0;
    right: 0;
    text-align: center;
    color: var(--brand-green);
  }
  .contact-address { right: 12px; text-align: left; }
  .card-back {
    position: absolute;
    left: 43px;
    top: 604px;
    width: 1004px;
    height: 539px;
    background: linear-gradient(135deg, var(--pattern-dark) 0%, var(--pattern-green) 50%, var(--pattern-dark) 100%);
    display: flex;
    align-items: center;
    justify-content: center;
  }
  .back-name {
    font-size: 64px;
    color: var(--back-word);
    letter-spacing: -1px;
  }
</style>
</head>
<body>
<div class="canvas">
  <section class="card-front">
    <div class="front-panel">
      <div class="logo">
        <span class="logo-mark"></span>
        <span class="logo-name">LumaConsulting</span>
      </div>
      <div class="person">
        <div class="person-name">John Doe</div>
        <div class="person-title">Job Title</div>
      </div>
      <div class="contact-phones">
        Cell: (xxx) xxx-xxxx<br>
        Phone: (xxx) xxx-xxxx<br>
        Fax: (xxx) xxx-xxxx
      </div>
      <div class="contact-web">
        name@lumaconsulting.com<br>
        www.lumaconsulting.com
      </div>
      <div class="contact-address">
        1234 Some Street Name<br>
        Somewhere , ST xxxxx
      </div>
    </div>
  </section>
  <section class="card-back" role="img" aria-label="Card back with a repeating diagonal pattern of the LumaConsulting name in green and grey on dark charcoal">
    <span class="back-name">LumaConsulting</span>
  </section>
</div>
</body>
</html>
```